Werbeflyer/Werbepostkarte für kleines Einzelunternehmen
Hallo Zusammen,
wir sind ein junges Unternehmen, welches überwiegend bayrische Accessoires designen und anfertigen. Unsere Zielgruppe sind sowohl Einzelhändler als auch der Endverbraucher. Insbesondere die feierwütige Gesellschaft der Volksfeste.
Da wir noch recht unbekannt sind, wollen wir durch die Flyer unseren Bekanntheitsgrad steigern und die Flyer auf Volksfesten oder im Einzelhandel verteilen/auslegen lassen.
Aufgabenstellung
Wir stellen uns einen Werbeflyer in Postkartenformat (A6) vor, der beidseitig bedruckt ist. Auf der Vorderseite sollen unsere Produkte so präsentiert werden, dass deutlich wird, was dieses Produkt darstellt und wofür es verwendet werden soll. Dabei beziehe ich mich vor allem auf die "Zwirnel-Ringe", welche zum einen als modisches Accessoires am Handgelenk fundieren und zum anderen als Bierkrug-Markierband. (Produktbilder sind dem Anhang beigefügt)
Zusätzlich soll ein schlichter Schriftzug darauf aufmerksam machen, dass man sich die Zwirnel-Ringe selber generieren/zusammenstellen/designen lassen kann, sodass sie zu jeder Tracht bzw. zu jedem Outfit individuell passen.
Gerne würden wir auch noch die Schlüsselbänder (ein Bild ist ausreichend) mit unterbringen, sodass erkenntlich wird, dass wir nicht nur die Zwirnel-Ringe produzieren, sondern auch andere bayerisch-angehauchte Accessoires.
Zum Schluss soll unser Logo noch mit untergebracht werden.
Die Rückseite soll schlicht gehalten werden und das Layout einer Postkartenrückseite abbilden. Ein Hinweis auf die Firma ( Logo, Adresse, Telefon, E-Mailadresse, Internetadresse) soll ebenfalls abgebildet werden.
Das ganze Design sollte insgesamt sehr schlicht und vintagemäßig von der Farbwahl gehalten werden. Am schönsten wäre es, wenn der Flyer durch sein Design den Zweck einer Postkarte erfüllt und verschickt wird.
Sollten sie noch weitere Materialien, Bilder, etc. benötigen oder noch offene Fragen zu meinen Angaben sind, bitte ich Sie mich einfach zu kontaktieren.
Vielen lieben Dank schonmal im Voraus.

```html
<!DOCTYPE html>
<html lang="de">
<head>
<meta charset="utf-8">
<title>Hanni Zierwerk – Postkarte</title>
<link rel="stylesheet" href="https://fonts.googleapis.com/css2?family=Fira+Sans:wght@400&family=Courgette&display=swap">
<style>
:root{
  --paper:#ffffff;
  --cream:#e6ebd4;
  --brown:#54463f;
  --ink:#2f2622;
  --text:#2b2b2b;
  --meadow:#a3bb5a;
  --check-light:#dfe0b8;
  --check-mid:#bcc680;
  --frame:#cbbb8e;
  --frame-dark:#a8946a;
  --line:#555;
}
*{box-sizing:border-box;margin:0;padding:0}
html,body{width:1004px;height:1200px;overflow:hidden;background:var(--paper)}
body{position:relative;font-family:"Fira Sans",sans-serif;color:var(--text)}
.card{position:absolute;left:238px;width:500px;height:354px;border:1px solid #222;overflow:hidden;background:var(--cream)}
.card--brown{top:43px}
.card--green{top:424px}
.card--back{top:804px;background:var(--paper)}
.check-band{position:absolute;left:0;top:0;width:100%;height:45px;
  background:linear-gradient(180deg,var(--check-mid) 0%,var(--check-light) 100%)}
.band{position:absolute;left:0;top:45px;width:100%;height:87px}
.band--brown{background:var(--brown)}
.band--green{background:var(--meadow)}
.stitch{position:absolute;left:0;width:100%;border-top:1px dashed rgba(255,255,255,.9)}
.foot{position:absolute;left:0;bottom:0;width:100%;height:20px}
.foot--brown{background:var(--brown)}
.foot--green{background:var(--meadow)}
.photo{position:absolute;border:6px solid var(--frame);box-shadow:0 2px 4px rgba(0,0,0,.35),inset 0 0 0 1px var(--frame-dark)}
.photo--wrist{left:31px;top:11px;width:136px;height:186px;transform:rotate(-5deg);
  background:linear-gradient(100deg,#e8e4dc 0%,#c9c1b0 35%,#d8cfe0 55%,#f4f2ef 100%)}
.photo--mug{left:160px;top:22px;width:100px;height:154px;transform:rotate(2deg);
  background:linear-gradient(90deg,#e6e4df 0%,#a8a295 40%,#8c877c 70%,#b9b3a7 100%)}
.photo--keys{left:318px;top:62px;width:186px;height:140px;transform:rotate(3deg);
  background:linear-gradient(180deg,#8b6e5a 0%,#9c8d7d 35%,#7e776e 65%,#6b665f 100%)}
.badge{position:absolute;width:36px;height:36px;border-radius:50%;background:#fff;border:2px solid #333;box-shadow:0 0 0 2px #fff,0 0 0 3px #777}
.badge--wrist{left:135px;top:156px}
.badge--mug{left:193px;top:168px}
.script{position:absolute;font-family:"Courgette",cursive;font-weight:400;color:var(--ink);font-size:16px;line-height:1;letter-spacing:-.3px;white-space:nowrap}
.copy{position:absolute;font-size:10.5px;line-height:14px;color:var(--text);white-space:nowrap}
.h-rings{left:49px;top:209px}
.h-keys{left:315px;top:209px}
.h-custom{left:51px;top:273px}
.c-rings{left:51px;top:230px}
.c-custom{left:51px;top:296px}
.brand{position:absolute;left:372px;top:278px;font-size:15px;color:var(--ink);white-space:nowrap}
.url{position:absolute;left:338px;top:311px;font-size:9.5px;color:var(--ink);white-space:nowrap}
.brand-back{position:absolute;left:60px;top:44px;font-size:15px;color:var(--ink);white-space:nowrap}
.divider{position:absolute;left:254px;top:63px;width:1px;height:243px;background:var(--line)}
.addr-line{position:absolute;left:274px;width:183px;height:1px;background:var(--line)}
.contact{position:absolute;left:0;width:246px;top:290px;text-align:center;font-size:7.5px;line-height:10px;color:var(--ink);white-space:nowrap}
</style>
</head>
<body>

<section class="card card--brown">
  <div class="check-band" role="img" aria-label="Karomuster in Grüntönen"></div>
  <div class="band band--brown"></div>
  <div class="stitch" style="top:49px"></div>
  <div class="stitch" style="top:126px"></div>
  <div class="photo photo--wrist" role="img" aria-label="Produktfoto: Zwirnel-Ring als Armband mit Herzanhänger"></div>
  <div class="photo photo--mug" role="img" aria-label="Produktfoto: Zwirnel-Ring am Henkel eines Bierkrugs"></div>
  <div class="badge badge--wrist" role="img" aria-label="Symbol Handgelenk"></div>
  <div class="badge badge--mug" role="img" aria-label="Symbol Bierkrug"></div>
  <div class="photo photo--keys" role="img" aria-label="Produktfoto: Schlüsselband mit roter Schleife auf Holz"></div>
  <h2 class="script h-rings">Zwirnel-Ringe</h2>
  <p class="copy c-rings">Als Schmuck für das Handgelenk<br>oder als Bierkrugmarkierung.</p>
  <h2 class="script h-custom">Dein persönlicher Zwirnel-Ring</h2>
  <p class="copy c-custom">Gestalte Deinen eigenen Zwirnel-Ring!<br>Individuell, passend zu Deiner Tracht.</p>
  <h2 class="script h-keys">Schlüsselbänder</h2>
  <p class="brand">Hanni Zierwerk</p>
  <p class="url">www.hanni-zierwerk.example</p>
  <div class="foot foot--brown"></div>
  <div class="stitch" style="top:339px"></div>
</section>

<section class="card card--green">
  <div class="check-band" role="img" aria-label="Karomuster in Grüntönen"></div>
  <div class="band band--green"></div>
  <div class="stitch" style="top:49px"></div>
  <div class="stitch" style="top:126px"></div>
  <div class="photo photo--wrist" role="img" aria-label="Produktfoto: Zwirnel-Ring als Armband mit Herzanhänger"></div>
  <div class="photo photo--mug" role="img" aria-label="Produktfoto: Zwirnel-Ring am Henkel eines Bierkrugs"></div>
  <div class="badge badge--wrist" role="img" aria-label="Symbol Handgelenk"></div>
  <div class="badge badge--mug" role="img" aria-label="Symbol Bierkrug"></div>
  <div class="photo photo--keys" role="img" aria-label="Produktfoto: Schlüsselband mit roter Schleife auf Holz"></div>
  <h2 class="script h-rings">Zwirnel-Ringe</h2>
  <p class="copy c-rings">Als Schmuck für das Handgelenk<br>oder als Bierkrugmarkierung.</p>
  <h2 class="script h-custom">Dein persönlicher Zwirnel-Ring</h2>
  <p class="copy c-custom">Gestalte Deinen eigenen Zwirnel-Ring!<br>Individuell, passend zu Deiner Tracht.</p>
  <h2 class="script h-keys">Schlüsselbänder</h2>
  <p class="brand">Hanni Zierwerk</p>
  <p class="url">www.hanni-zierwerk.example</p>
  <div class="foot foot--green" role="img" aria-label="Zierborte mit Bogenmuster"></div>
</section>

<section class="card card--back">
  <p class="brand-back">Hanni Zierwerk</p>
  <div class="divider"></div>
  <div class="addr-line" style="top:150px"></div>
  <div class="addr-line" style="top:192px"></div>
  <div class="addr-line" style="top:235px"></div>
  <p class="contact">Lenbachweg 12 // 80000 Musterstadt<br>info@hanni-zierwerk.example // www.hanni-zierwerk.example</p>
</section>

</body>
</html>
```